Brisk Valets Postcard - I would like to send this using MAIL to my prospects and current clients.

This store is under new management. I would like to design a high end postcard that showcases our services. Here is a list of the services that we provide to our customers.
- Premium Organic Dry Cleaning
- Laundered Shirts
- Expert Alterations
- Shoes and Leather Repairs by Tenby Partners
- Area Rug Cleaning by Harlow Launderers
- Leather and Suede Cleaning by Pike Launderers
- Household Items
- Wedding Dress Cleaning and Preservation
I would like to offer 10% off (one-time use) coupon as well as 20% off to new customers.
Here is a logo file with location details.
While designing postcards, I would like to showcase stack of different garments (Season based) and household items. Also, use the colors that I have provided in the logo design.
We also offer Free Pick up and delivery.
About Us:
Brisk Valets is a premium dry cleaning and garment care service dedicated to delivering exceptional quality, convenience, and personalized attention. Located in the heart of Bedminster, NJ, we specialize in eco-friendly dry cleaning, expert stain removal, professional garment pressing, and specialized care for delicate fabrics, designer clothing, household items, and formal wear.
Our mission is to provide reliable, high-quality service while preserving the longevity and appearance of our customers’ garments. With state-of-the-art equipment, experienced staff, and a commitment to customer satisfaction, Brisk Valets ensures your clothing looks and feels its best — every time.
We also offer convenient services such as same-day cleaning, alterations, wash & fold, and pickup and delivery options, making garment care simple and hassle-free for our busy clientele.
Experience the difference with Brisk Valets — where luxury care meets everyday convenience.

Target Market(s)

Household above $100K

Industry/Entity Type

Dry Cleaning

Font styles to use
Serif

Colors
0054AA
0677BA
7BADD7
CADEEF
E8F1F8
FFC000
F8CF3A
FAE287
FDF2CF
FEFAEE

Requirements
Must have
• Elegant Design with stacked clothes, highlight Organic Dry Cleaning store. The color schemes should have these colors. D4AF37 (Fonts), 0D1B2A (Background). These are used in my logo and tagline.
Nice to have
• On the backside I would like to show our location on the map, streets

```html
<!DOCTYPE html>
<html lang="en">
<head>
<meta charset="utf-8">
<title>Brisk Valets Postcard</title>
<link rel="stylesheet" href="https://fonts.googleapis.com/css2?family=Playfair+Display:ital,wght@0,500;1,700;1,900&family=Poppins:ital,wght@0,400;0,500;0,600;0,700;1,400&family=Russo+One&family=Tinos:wght@700&display=swap">
<style>
  :root {
    --navy: #0d1b2a;
    --navy-mid: #123a63;
    --navy-deep: #0f2a47;
    --gold: #d4af37;
    --gold-panel: #cfaa33;
    --coupon-blue: #0054aa;
    --white: #ffffff;
    --page: #ececec;
    --silver-hi: #ffffff;
    --silver-mid: #c3c9d2;
    --silver-lo: #7e8896;
  }
  * { box-sizing: border-box; margin: 0; padding: 0; }
  html, body { width: 864px; height: 1200px; overflow: hidden; }
  body { background: var(--page); position: relative; font-family: "Poppins", sans-serif; }

  .card { position: absolute; left: 42px; width: 780px; height: 557px; overflow: hidden; }
  .card-front { top: 28px; background: linear-gradient(135deg, var(--navy-mid) 0%, var(--navy-deep) 70%, var(--navy) 100%); }
  .card-back { top: 615px; background: var(--white); }

  /* ---------- Front ---------- */
  .brand-panel { position: absolute; right: 0; top: 0; width: 170px; height: 170px; background: var(--navy); }
  .brand-name { position: absolute; right: 0; top: 52px; width: 170px; text-align: center;
    font-family: "Playfair Display", serif; font-weight: 500; font-size: 19px; line-height: 1.15;
    letter-spacing: 1px; color: var(--gold); }

  .headline { position: absolute; left: 0; top: 0; }
  .headline span { position: absolute; white-space: nowrap; font-family: "Playfair Display", serif; font-style: italic; }
  .silver { font-weight: 700;
    background: linear-gradient(180deg, var(--silver-hi) 10%, var(--silver-mid) 48%, var(--silver-lo) 55%, #e6e9ee 90%);
    -webkit-background-clip: text; background-clip: text; color: transparent;
    filter: drop-shadow(2px 3px 2px rgba(0,0,0,.45)); }
  .h-premium { left: 140px; top: 22px; font-size: 50px; }
  .h-organic { left: 34px; top: 34px; font-size: 100px; font-weight: 900; color: var(--gold);
    filter: drop-shadow(2px 3px 2px rgba(0,0,0,.4)); }
  .h-dry { left: 210px; top: 118px; font-size: 58px; }
  .h-cleaning { left: 50px; top: 160px; font-size: 86px; }

  .services { position: absolute; left: 0; top: 285px; width: 466px; height: 172px; background: var(--gold-panel);
    clip-path: polygon(0 0, 100% 0, 100% 80%, 94% 100%, 0 100%); }
  .service-list { position: absolute; top: 24px; list-style: none; display: flex; flex-direction: column; gap: 9px; }
  .service-list.col-a { left: 35px; width: 195px; }
  .service-list.col-b { left: 239px; width: 215px; }
  .service-list li { position: relative; padding-left: 16px; color: var(--white); font-size: 12.8px; font-weight: 500; line-height: 1.3; }
  .service-list svg { position: absolute; left: 0; top: 3px; width: 11px; height: 11px; }

  .garment-stack { position: absolute; left: 473px; top: 120px; width: 273px; height: 340px;
    clip-path: polygon(16% 0, 100% 0, 100% 100%, 0 100%, 0 18%, 16% 10%);
    background: linear-gradient(170deg, #c9c8c6 0%, #d8b7ad 25%, #e07c95 42%, #6fa3cf 58%, #e2b548 72%, #7fb5c4 86%, #a7485a 100%); }

  .call-bar { position: absolute; left: 35px; top: 483px; width: 419px; height: 46px; border-radius: 23px;
    background: var(--white); display: flex; align-items: center; overflow: hidden; }
  .call-label { height: 100%; width: 122px; background: var(--gold); border-radius: 23px 0 0 23px;
    display: flex; align-items: center; justify-content: center;
    font-family: "Russo One", sans-serif; font-size: 28px; color: var(--white); letter-spacing: 1px; }
  .call-number { flex: 1; text-align: center; font-family: "Russo One", sans-serif; font-size: 32px; color: var(--navy); letter-spacing: 1px; }

  .delivery { position: absolute; left: 475px; top: 488px; height: 45px; display: flex; align-items: center; }
  .scooter { width: 62px; height: 45px; border-radius: 6px; background: linear-gradient(135deg, #d33a2c, #2e6b3a); }
  .free-tag { margin-left: 4px; height: 38px; padding: 0 10px; background: var(--gold); display: flex; align-items: center;
    font-family: "Russo One", sans-serif; font-size: 27px; color: var(--white); }
  .pickup-tag { height: 38px; padding: 0 8px; border: 1.5px solid var(--white); border-left: none; display: flex; align-items: center;
    font-family: "Russo One", sans-serif; font-size: 12.5px; line-height: 1.05; color: var(--white); }

  /* ---------- Back ---------- */
  .about-title { position: absolute; left: 37px; top: 22px; font-weight: 700; font-size: 23px; color: var(--gold); }
  .about-panel { position: absolute; left: 0; top: 48px; width: 454px; height: 346px; background: var(--gold-panel);
    clip-path: polygon(0 0, 92% 0, 100% 11%, 100% 100%, 0 100%); }
  .about-text { position: absolute; left: 36px; top: 76px; width: 368px; color: var(--white); font-size: 11.6px; line-height: 1.32; text-align: justify; }
  .about-text p { margin-bottom: 7px; }
  .about-text strong { font-weight: 700; }
  .about-text em { font-style: italic; }

  .location-map { position: absolute; left: 489px; top: 30px; width: 198px; height: 283px;
    background: linear-gradient(160deg, #ececec 0%, #f4efe2 45%, #e6e6e6 100%); }

  .contact-strip { position: absolute; left: 35px; top: 394px; width: 680px; height: 124px; background: var(--navy);
    clip-path: polygon(0 0, 96% 0, 100% 16%, 100% 100%, 0 100%); }
  .contact-brand { position: absolute; left: 52px; top: 448px; width: 110px; text-align: center;
    font-family: "Playfair Display", serif; font-weight: 500; font-size: 18px; line-height: 1.15; letter-spacing: 1px; color: var(--gold); }
  .contact-divider { position: absolute; left: 180px; top: 412px; width: 1px; height: 90px; background: rgba(255,255,255,.35); }
  .contact-address { position: absolute; left: 195px; top: 416px; display: flex; gap: 9px; color: var(--white);
    font-family: "Tinos", serif; font-weight: 700; font-size: 15.5px; line-height: 1.2; }
  .contact-phone { position: absolute; left: 195px; top: 468px; display: flex; align-items: center; gap: 12px; color: var(--white);
    font-family: "Tinos", serif; font-weight: 700; font-size: 29px; }
  .contact-rule { position: absolute; left: 218px; top: 461px; width: 220px; height: 1px; background: rgba(255,255,255,.3); }

  .laundry-basket { position: absolute; left: 432px; top: 262px; width: 212px; height: 272px;
    clip-path: polygon(8% 0, 92% 4%, 100% 30%, 97% 100%, 6% 100%, 0 30%);
    background: linear-gradient(180deg, #c8b3a4 0%, #d9a0a4 20%, #9fcfc7 35%, #b88a55 48%, #a77b45 75%, #8e6634 100%); }

  .coupons { position: absolute; left: 689px; top: 27px; }
</style>
</head>
<body>

<section class="card card-front" aria-label="Postcard front">
  <div class="brand-panel"></div>
  <div class="brand-name">BRISK<br>VALETS</div>

  <h1 class="headline" aria-label="Premium Organic Dry Cleaning">
    <span class="silver h-premium">Premium</span>
    <span class="h-organic">Organic</span>
    <span class="silver h-dry">Dry</span>
    <span class="silver h-cleaning">Cleaning</span>
  </h1>

  <div class="garment-stack" role="img" aria-label="Stack of folded colourful seasonal garments"></div>

  <div class="services">
    <ul class="service-list col-a">
      <li><svg viewBox="0 0 12 12"><circle cx="6" cy="6" r="5" fill="none" stroke="#fff" stroke-width="1.2"/><path d="M3.5 6.2l1.7 1.6 3.3-3.4" fill="none" stroke="#fff" stroke-width="1.2"/></svg>Laundered Shirts</li>
      <li><svg viewBox="0 0 12 12"><circle cx="6" cy="6" r="5" fill="none" stroke="#fff" stroke-width="1.2"/><path d="M3.5 6.2l1.7 1.6 3.3-3.4" fill="none" stroke="#fff" stroke-width="1.2"/></svg>Expert Alterations</li>
      <li><svg viewBox="0 0 12 12"><circle cx="6" cy="6" r="5" fill="none" stroke="#fff" stroke-width="1.2"/><path d="M3.5 6.2l1.7 1.6 3.3-3.4" fill="none" stroke="#fff" stroke-width="1.2"/></svg>Shoes and Leather Repairs by Tenby Partners</li>
      <li><svg viewBox="0 0 12 12"><circle cx="6" cy="6" r="5" fill="none" stroke="#fff" stroke-width="1.2"/><path d="M3.5 6.2l1.7 1.6 3.3-3.4" fill="none" stroke="#fff" stroke-width="1.2"/></svg>Household Items</li>
    </ul>
    <ul class="service-list col-b">
      <li><svg viewBox="0 0 12 12"><circle cx="6" cy="6" r="5" fill="none" stroke="#fff" stroke-width="1.2"/><path d="M3.5 6.2l1.7 1.6 3.3-3.4" fill="none" stroke="#fff" stroke-width="1.2"/></svg>Area Rug Cleaning by Harlow Launderers</li>
      <li><svg viewBox="0 0 12 12"><circle cx="6" cy="6" r="5" fill="none" stroke="#fff" stroke-width="1.2"/><path d="M3.5 6.2l1.7 1.6 3.3-3.4" fill="none" stroke="#fff" stroke-width="1.2"/></svg>Leather and Suede Cleaning by Pike Launderers</li>
      <li><svg viewBox="0 0 12 12"><circle cx="6" cy="6" r="5" fill="none" stroke="#fff" stroke-width="1.2"/><path d="M3.5 6.2l1.7 1.6 3.3-3.4" fill="none" stroke="#fff" stroke-width="1.2"/></svg>Wedding Dress Cleaning and Preservation</li>
    </ul>
  </div>

  <div class="call-bar">
    <div class="call-label">CALL</div>
    <div class="call-number">0198 765 432</div>
  </div>

  <div class="delivery">
    <div class="scooter" role="img" aria-label="Courier riding a delivery scooter"></div>
    <div class="free-tag">FREE</div>
    <div class="pickup-tag">PICK UP &amp;<br>DELIVERY</div>
  </div>
</section>

<section class="card card-back" aria-label="Postcard back">
  <h2 class="about-title">ABOUT US:</h2>
  <div class="about-panel"></div>
  <div class="about-text">
    <p><strong>Brisk Valets</strong> is a premium dry cleaning and garment care service dedicated to delivering exceptional quality, convenience, and personalized attention. Located in the heart of Larkmoor, NJ, we specialize in eco-friendly dry cleaning, expert stain removal, professional garment pressing, and specialized care for delicate fabrics, designer clothing, household items, and formal wear.</p>
    <p><strong>Our mission is to provide reliable, high-quality service</strong> while preserving the longevity and appearance of our customers’ garments. With state-of-the-art equipment, experienced staff, and a commitment to customer satisfaction, Brisk Valets ensures your clothing looks and feels its best — every time.</p>
    <p><strong>We also offer</strong> convenient services such as same-day cleaning, alterations, wash &amp; fold, and pickup and delivery options, making garment care simple and hassle-free for our busy clientele.</p>
    <p><em>Experience the difference with Brisk Valets — where luxury care meets everyday convenience.</em></p>
  </div>

  <div class="location-map" role="img" aria-label="Street map showing the store location"></div>

  <svg class="coupons" width="76" height="355" viewBox="0 0 76 355" aria-label="Coupons: 10% off one-time use, 20% off new customers">
    <defs>
      <pattern id="perforation" width="76" height="10" patternUnits="userSpaceOnUse">
        <circle cx="0" cy="5" r="3.2" fill="#fff"/>
        <circle cx="76" cy="5" r="3.2" fill="#fff"/>
      </pattern>
    </defs>
    <rect x="0" y="0" width="76" height="118" fill="var(--coupon-blue)"/>
    <rect x="0" y="118" width="76" height="60" fill="var(--gold)"/>
    <rect x="0" y="184" width="76" height="106" fill="var(--coupon-blue)"/>
    <rect x="0" y="290" width="76" height="65" fill="var(--gold)"/>
    <circle cx="38" cy="181" r="8" fill="#fff"/>
    <rect x="0" y="0" width="76" height="355" fill="url(#perforation)"/>

    <g font-family="Russo One, sans-serif" fill="#fff">
      <text transform="translate(51,72) rotate(-90)" text-anchor="middle" font-size="38">10%</text>
      <text transform="translate(51,238) rotate(-90)" text-anchor="middle" font-size="38">20%</text>
    </g>
    <g font-family="Poppins, sans-serif" font-weight="700">
      <rect x="13" y="10" width="11" height="22" fill="var(--gold)"/>
      <text transform="translate(21.5,21) rotate(-90)" text-anchor="middle" font-size="7.5" fill="#fff">OFF</text>
      <rect x="13" y="192" width="11" height="22" fill="var(--gold)"/>
      <text transform="translate(21.5,203) rotate(-90)" text-anchor="middle" font-size="7.5" fill="#fff">OFF</text>
      <text transform="translate(64,60) rotate(-90)" text-anchor="middle" font-size="6.5" fill="#fff">ONE-TIME USE</text>
      <text transform="translate(64,238) rotate(-90)" text-anchor="middle" font-size="6.5" fill="#fff">NEW CUSTOMERS</text>
    </g>
    <g font-family="Russo One, sans-serif" fill="var(--navy)">
      <text transform="translate(33,148) rotate(90)" text-anchor="middle" font-size="13">OFFER</text>
      <text transform="translate(33,322) rotate(90)" text-anchor="middle" font-size="13">OFFER</text>
    </g>
  </svg>

  <div class="contact-strip"></div>
  <div class="contact-brand">BRISK<br>VALETS</div>
  <div class="contact-divider"></div>
  <div class="contact-address">
    <svg width="12" height="16" viewBox="0 0 12 16" aria-hidden="true"><path d="M6 1a4.6 4.6 0 0 0-4.6 4.6C1.4 9.3 6 15 6 15s4.6-5.7 4.6-9.4A4.6 4.6 0 0 0 6 1z" fill="none" stroke="#d4af37" stroke-width="1.3"/><circle cx="6" cy="5.6" r="1.7" fill="none" stroke="#d4af37" stroke-width="1.3"/></svg>
    <span>48 Orchard Hill Road<br>Larkmoor, NJ 07945</span>
  </div>
  <div class="contact-rule"></div>
  <div class="contact-phone">
    <svg width="22" height="22" viewBox="0 0 24 24" aria-hidden="true"><path d="M6.6 2.5l3 3.6-1.9 2.3a12 12 0 0 0 7.9 7.9l2.3-1.9 3.6 3-1.8 3.2c-.4.7-1.2 1-2 .8C10 19.9 4.1 14 2.6 6.4c-.2-.8.1-1.6.8-2z" fill="none" stroke="#d4af37" stroke-width="1.6" stroke-linejoin="round"/></svg>
    <span>0198 765 432</span>
  </div>

  <div class="laundry-basket" role="img" aria-label="Wicker basket filled with towels and household linens"></div>
</section>

</body>
</html>
```